Electrician's Business needs web site for customers to get professional impression of business.

Have a logo, need a web page for customers to visit. Web page should make it easy for customers to approach /contact me, if possible a way for customers to leave their details so I can call them back.
A description/ list of services and advertise how my service is different and better than other electricians.
A gallery to upload photos to, to show completed works from past projects.

Target Market(s)

Domestic/residential home owner/renter/builder

Industry/Entity Type

Electrician

Coding

Coded - Design and coding required

Number of Pages Required

2 page

Font styles to use
Sans Serif

Colors
0255a3
ffffff

Requirements
Must have
• Appeal to home owner/renter, domestic market.
• Capture contact details of customer & advertise my contact details.
• List of services
Nice to have
• A photo gallery, so I can upload pictures of completed work.
Should not have
• Industrial/construction images.

```html
<!DOCTYPE html>
<html lang="en">
<head>
<meta charset="utf-8">
<title>Brightwire Electrical Services</title>
<link href="https://fonts.googleapis.com/css2?family=Montserrat:wght@400;600;700;800&family=Raleway:wght@300;400;500&display=swap" rel="stylesheet">
<style>
:root{
  --blue:#0255a3;
  --blue-dark:#013f7c;
  --orange:#f07f1b;
  --white:#ffffff;
  --grey-text:#a9a9a9;
  --heading-grey:#8f8f8f;
  --band-grey:#e4e6e8;
  --line:#d6d6d6;
}
*{box-sizing:border-box;margin:0;padding:0}
html,body{width:1200px;height:2773px;overflow:hidden}
body{position:relative;background:var(--white);font-family:"Raleway",Arial,sans-serif;color:var(--grey-text)}
.abs{position:absolute}
.btn{position:absolute;display:flex;align-items:center;justify-content:center;background:var(--orange);color:var(--white);font-family:"Montserrat",Arial,sans-serif;font-weight:600;font-size:13px}

/* header */
.top-rule{left:0;top:0;width:1200px;height:11px;background:var(--blue)}
.brand{left:131px;top:58px;color:var(--blue);font-family:"Montserrat",Arial,sans-serif;font-weight:700;line-height:1}
.brand-name{font-size:30px;letter-spacing:-.5px}
.brand-tag{font-size:11px;margin-top:4px;padding-left:40px}
.header-phone{left:690px;top:44px;width:176px;text-align:center;color:var(--blue);font-family:"Montserrat",Arial,sans-serif;font-weight:700;font-size:21px}
.header-phone svg{display:block;margin:0 auto 8px}
.quote-btn{left:926px;top:63px;width:141px;height:33px}

/* hero */
.hero{left:0;top:146px;width:1200px;height:440px;background:var(--blue);overflow:hidden}
.hero-photo{position:absolute;left:620px;top:0;width:580px;height:440px;background:linear-gradient(90deg,var(--blue) 0%,#4d7fb3 22%,#b9c3cc 55%,#d9dcde 100%)}
.hero-copy{position:absolute;left:131px;top:112px;color:var(--white);font-family:"Montserrat",Arial,sans-serif}
.hero-copy .welcome{font-size:33px;font-weight:400}
.hero-copy h1{font-size:66px;font-weight:800;line-height:1.05;margin-top:4px}
.hero-copy .sub{font-size:19px;font-weight:600;margin-top:12px}
.hero-read{left:131px;top:290px;width:141px;height:32px}
.hero-services{left:294px;top:290px;width:141px;height:32px}
.dots{left:555px;top:407px;display:flex;gap:18px}
.dots span{width:14px;height:14px;border-radius:50%;background:var(--white)}
.social{left:1159px;top:89px;width:41px}
.social span{display:flex;align-items:center;justify-content:center;width:41px;height:41px;margin-bottom:3px}

/* sections */
.section-title{position:absolute;left:0;width:1200px;text-align:center;font-family:"Montserrat",Arial,sans-serif;font-weight:700;font-size:38px;color:var(--heading-grey)}
.section-title::after{content:"";display:block;width:170px;height:3px;background:var(--orange);margin:4px auto 0}
.lede{position:absolute;left:131px;width:938px;text-align:center;font-size:18px;line-height:28px;font-weight:300}
.about-more{left:531px;top:899px;width:140px;height:32px}

.services-band{left:0;top:1189px;width:1200px;height:305px;background:var(--blue)}
.service-photo{position:absolute;top:74px;width:216px;height:166px}
.arrow{position:absolute;top:139px;width:33px;height:31px;background:var(--blue-dark);display:flex;align-items:center;justify-content:center}

.categories{left:360px;top:1733px;width:480px;display:flex;justify-content:space-between;font-family:"Montserrat",Arial,sans-serif;font-weight:700;font-size:13px;color:var(--blue)}
.categories .active{border-bottom:3px solid var(--orange);padding-bottom:4px}

.gallery-band{left:0;top:1797px;width:1200px;height:413px;background:var(--band-grey)}
.gallery{position:absolute;left:131px;top:0;width:936px;height:413px;display:grid;grid-template-columns:repeat(4,234px);grid-template-rows:repeat(2,206.5px)}
.tile{position:relative}
.tile-card{position:absolute;inset:16px;background:rgba(2,85,163,.88);color:var(--white);text-align:center;font-family:"Montserrat",Arial,sans-serif;padding-top:16px}
.tile-card .cat{font-size:14px;font-weight:700}
.tile-card .name{font-size:22px;font-weight:700;margin-top:6px}
.tile-card p{font-family:"Raleway",Arial,sans-serif;font-size:11px;line-height:14px;margin:14px 14px 0}

.emergency{left:0;top:2210px;width:1200px;height:142px;background:linear-gradient(90deg,#1a5f9f,#2c7fb8 45%,#1b6aa8 70%,#0e4d8c);display:flex;align-items:center;justify-content:center;color:var(--white);font-family:"Raleway",Arial,sans-serif;font-weight:400;font-size:37px}

/* footer */
.footer-col{position:absolute;top:2422px;width:216px;font-size:13px;line-height:20px;font-weight:400}
.footer-col h4{font-family:"Montserrat",Arial,sans-serif;font-weight:700;font-size:13px;color:var(--grey-text);margin-bottom:20px;letter-spacing:.3px}
.footer-brand{color:var(--blue);font-family:"Montserrat",Arial,sans-serif;font-weight:700;line-height:1;margin-bottom:22px}
.footer-brand .brand-name{font-size:27px}
.footer-brand .brand-tag{font-size:10px;margin-top:3px;padding-left:36px}
.service-list li{list-style:none;border-bottom:1px solid var(--line);height:31px;line-height:30px}
.contact p{margin-bottom:0}
.contact .gap{height:26px}
.contact a{color:var(--blue);font-weight:600;text-decoration:none}
.field{position:absolute;left:834px;width:233px;border:1px solid var(--line);font-size:12px;padding:4px 6px;color:var(--grey-text)}
.field.focus{border-color:#9bb6d6}
.send-btn{left:834px;top:2666px;width:141px;height:32px}
.copyright{left:0;top:2725px;width:1200px;height:48px;background:var(--blue);color:var(--white);display:flex;align-items:center;justify-content:center;font-size:14px;font-weight:500}
</style>
</head>
<body>
<div class="abs top-rule"></div>

<header>
  <div class="abs brand"><div class="brand-name">Brightwire</div><div class="brand-tag">Electrical Services</div></div>
  <div class="abs header-phone">
    <svg width="30" height="30" viewBox="0 0 30 30"><circle cx="15" cy="15" r="15" fill="#0255a3"/><path d="M10.5 8.5l3 3-1.6 1.8c.8 1.8 2.2 3.2 4 4l1.8-1.6 3 3-1.9 1.9c-4.8-.4-9.8-5.4-10.2-10.2z" fill="#f07f1b"/></svg>
    1-800-555-0147
  </div>
  <div class="btn quote-btn">Get a Quote</div>
</header>

<section class="abs hero">
  <div class="hero-photo" role="img" aria-label="Photo of an electrician's hands working on a fuse board"></div>
  <div class="hero-copy">
    <div class="welcome">Welcome to</div>
    <h1>Brightwire</h1>
    <div class="sub">An Electrical Service Provider</div>
  </div>
  <div class="btn hero-read">Read More</div>
  <div class="btn hero-services">Our Services</div>
  <div class="abs dots"><span></span><span></span><span></span></div>
  <div class="abs social">
    <span style="background:#3b5998"></span>
    <span style="background:#29a9e1"></span>
    <span style="background:#1fb57a"><svg width="16" height="12" viewBox="0 0 16 12"><rect x="0.5" y="0.5" width="15" height="11" fill="#fff"/><path d="M1 1l7 5 7-5" stroke="#1fb57a" stroke-width="1.4" fill="none"/></svg></span>
    <span style="background:#e8412f"><svg width="12" height="17" viewBox="0 0 12 17"><path d="M6 0a6 6 0 0 0-6 6c0 4.5 6 11 6 11s6-6.5 6-11a6 6 0 0 0-6-6z" fill="#fff"/><circle cx="6" cy="6" r="2.2" fill="#e8412f"/></svg></span>
    <span style="background:#8a5a44"></span>
  </div>
</section>

<section class="about">
  <h2 class="section-title" style="top:612px">About Us</h2>
  <p class="lede" style="top:700px">It is a long established fact that a reader will be distracted by the readable content of a page when looking at its layout. The point of using Lorem Ipsum is that it has a more-or-less normal distribution of letters, as opposed to using 'Content here, content here', making it look like readable English. Many desktop publishing packages and web page editors now use Lorem Ipsum as their default model text, and a search for 'lorem ipsum' will uncover many web sites still in their infancy. Various versions have evolved over the years, sometimes by accident, sometimes on purpose (injected humour and the like).</p>
  <div class="btn about-more">Read More</div>
</section>

<section class="services">
  <h2 class="section-title" style="top:976px">Our Services</h2>
  <p class="lede" style="top:1070px">It is a long established fact that a reader will be distracted by the readable content of a page when looking at its layout. The point of using Lorem Ipsum is that it has a more-or-less normal distribution of letters, as opposed to using 'Content here, content here', making it look like readable English.</p>
  <div class="abs services-band">
    <div class="arrow" style="left:98px"><svg width="12" height="10" viewBox="0 0 12 10"><path d="M5 0L0 5l5 5V6.5h7v-3H5z" fill="#fff"/></svg></div>
    <div class="service-photo" style="left:178px;background:linear-gradient(180deg,#cfd3d6,#7d8489)" role="img" aria-label="Photo of a lit commercial interior with ceiling lights"></div>
    <div class="service-photo" style="left:488px;background:linear-gradient(180deg,#8f9aa2,#4d5a63)" role="img" aria-label="Photo of electrical switchgear cabinets"></div>
    <div class="service-photo" style="left:801px;background:linear-gradient(180deg,#c9b8a6,#8e7a68)" role="img" aria-label="Photo of an electrician fitting wiring in a ceiling"></div>
    <div class="arrow" style="left:1069px"><svg width="12" height="10" viewBox="0 0 12 10"><path d="M7 0l5 5-5 5V6.5H0v-3h7z" fill="#fff"/></svg></div>
  </div>
</section>

<section class="projects">
  <h2 class="section-title" style="top:1533px">Recent Projects</h2>
  <p class="lede" style="top:1621px">It is a long established fact that a reader will be distracted by the readable content of a page when looking at its layout. The point of using Lorem Ipsum is that it has a more-or-less normal distribution of letters, as opposed to using 'Content here, content here', making it look like readable English.</p>
  <nav class="abs categories"><span class="active">CATEGORY 1</span><span>CATEGORY 2</span><span>CATEGORY 3</span><span>CATEGORY 4</span></nav>
  <div class="abs gallery-band">
    <div class="gallery">
      <div class="tile" style="background:linear-gradient(135deg,#5d7da0,#2b4d74)" role="img" aria-label="Photo of a completed distribution board">
        <div class="tile-card"><div class="cat">CATEGORY 1</div><div class="name">Project Name</div><p>It is a long established fact that a reader will be distracted by the readable content of a page when looking at its layout.</p></div>
      </div>
      <div class="tile" style="background:linear-gradient(135deg,#c9a542,#5b5f63)" role="img" aria-label="Photo of gloved hands wiring a panel"></div>
      <div class="tile" style="background:linear-gradient(135deg,#b24a3e,#6e7d86)" role="img" aria-label="Photo of a multimeter testing a terminal block"></div>
      <div class="tile" style="background:linear-gradient(135deg,#9ba3a8,#d3a24a)" role="img" aria-label="Photo of a multimeter in use on a circuit"></div>
      <div class="tile" style="background:linear-gradient(135deg,#d3b13b,#4e6f93)" role="img" aria-label="Photo of a voltage tester on a fuse board"></div>
      <div class="tile" style="background:linear-gradient(135deg,#c9a93a,#6b5648)" role="img" aria-label="Photo of an electrician in a hard hat at work"></div>
      <div class="tile" style="background:linear-gradient(135deg,#f0f0f0,#2e4f7c)" role="img" aria-label="Photo of an electrician team standing together"></div>
      <div class="tile" style="background:linear-gradient(135deg,#d6d9dc,#8c6a52)" role="img" aria-label="Photo of hands using pliers on circuit breakers"></div>
    </div>
  </div>
</section>

<div class="abs emergency" role="img" aria-label="Background photo of cables and fuses in blue tones"><span>24/7 Emergency Electrician - Call 1-800-555-0147</span></div>

<footer>
  <div class="footer-col" style="left:131px">
    <h4>ABOUT COMPNAY</h4>
    <div class="footer-brand"><div class="brand-name">Brightwire</div><div class="brand-tag">Electrical Services</div></div>
    <p>Lorem ipsum dolor sit amet, con adipiscing elit. Aienean ac libor eu lobortis risus. Nunc bibendum eros iac dui dig eget accumsan magna tristique.</p>
  </div>
  <div class="footer-col" style="left:366px">
    <h4>SERVICES</h4>
    <ul class="service-list">
      <li>Industrial &amp; Building</li>
      <li>Electrification.</li>
      <li>Planning &amp; Installation.</li>
      <li>Installation of H.T. Panel.</li>
      <li>Installation of L.T. Panel</li>
      <li>Installation of Light Fixtures.</li>
    </ul>
  </div>
  <div class="footer-col contact" style="left:599px">
    <h4>CONTACT US</h4>
    <p>Leeds, UK</p>
    <p>41, Elm Row, Ashford Hills</p>
    <div class="gap"></div>
    <p>Tel: (888) 555-0192</p>
    <p>Mobile: (012) 555-0136</p>
    <div class="gap"></div>
    <p>E-mail: hello@brightwire.example</p>
    <p><a>Get directions on the map</a></p>
  </div>
  <div class="footer-col" style="left:834px"><h4>GET FREE QUOTE</h4></div>
  <div class="field focus" style="top:2452px;height:26px">Name</div>
  <div class="field" style="top:2487px;height:26px">Email</div>
  <div class="field" style="top:2526px;height:26px;display:flex;justify-content:space-between;align-items:center">Service<svg width="9" height="6" viewBox="0 0 9 6"><path d="M0 0h9L4.5 6z" fill="#a9a9a9"/></svg></div>
  <div class="field" style="top:2565px;height:79px">Message</div>
  <div class="btn send-btn">Send</div>
  <div class="abs copyright">© 2016 Brightwire | Electrical Services !</div>
</footer>
</body>
</html>
```